Marrowgate Auctions Business Cards Design Needed

I need a business card design that is modern looking - double sided (maybe just my logo on the back, but open to suggestions) - the overall design is up to you. I want it to be easy to read - not over the top flashy. I already have a company logo which I uploaded so that needs to be used. The colors of my logo are the colors I want on the card... so blue and gray (do need to match the logo colors).

Requirements
Must have
• Would like the card to be sleek, modern and easy to ready

```html
<!DOCTYPE html>
<html lang="en">
<head>
<meta charset="utf-8">
<title>Marrowgate Auctions – Business Cards</title>
<link rel="stylesheet" href="https://fonts.googleapis.com/css2?family=Roboto:wght@400;700&family=Roboto+Condensed:wght@400&family=Crimson+Text:ital@1&display=swap">
<style>
  :root {
    --page: #e9edf1;
    --card: #ffffff;
    --ink-gray: #4a4c4f;
    --ink-dark: #3a3b3d;
    --brand-blue: #2a73c0;
    --bright-blue: #1f6fe8;
    --pale-blue: #cfe3fb;
    --shadow: rgba(30, 45, 60, 0.22);
  }
  html, body {
    margin: 0;
    width: 1200px;
    height: 1187px;
    overflow: hidden;
    background: var(--page);
  }
  .canvas {
    position: relative;
    width: 1200px;
    height: 1187px;
  }
  .card {
    position: absolute;
    width: 640px;
    height: 366px;
    background: var(--card);
    box-shadow: 0 6px 18px var(--shadow);
    overflow: hidden;
    font-family: "Roboto", Arial, sans-serif;
  }
  .card--front { left: 470px; top: 170px; }
  .card--back  { left: 90px;  top: 640px; }

  .shard-band {
    position: absolute;
    background: linear-gradient(100deg, var(--bright-blue) 0%, #5aa0f2 35%, var(--pale-blue) 65%, rgba(255,255,255,0) 95%);
    opacity: 0.9;
  }
  .card--front .shard-band { left: 0; bottom: 40px; width: 560px; height: 120px; }
  .card--back .shard-band  { left: 0; top: 190px; width: 400px; height: 150px; }

  /* Front */
  .brand {
    position: absolute;
    left: 0; right: 0; top: 108px;
    text-align: center;
  }
  .brand__name {
    display: inline-flex;
    align-items: center;
    gap: 12px;
    font-weight: 700;
    font-size: 38px;
    letter-spacing: 0.5px;
    color: var(--ink-gray);
    text-transform: uppercase;
  }
  .brand__mark {
    width: 26px; height: 26px;
    background: var(--brand-blue);
  }
  .brand__tagline {
    margin-top: 6px;
    font-family: "Crimson Text", Georgia, serif;
    font-style: italic;
    font-size: 21px;
    color: var(--brand-blue);
  }

  /* Back */
  .person {
    position: absolute;
    left: 60px; top: 58px;
  }
  .person__name {
    font-weight: 700;
    font-size: 40px;
    letter-spacing: 2px;
    color: var(--ink-dark);
    line-height: 1;
  }
  .person__name span { font-weight: 400; }
  .person__title {
    margin-top: 6px;
    font-family: "Roboto Condensed", Arial, sans-serif;
    font-size: 19px;
    color: var(--brand-blue);
    padding-bottom: 4px;
    border-bottom: 2px solid var(--ink-dark);
    position: relative;
    width: 100%;
  }
  .person__title::after {
    content: "";
    position: absolute;
    left: 0; bottom: -5px;
    width: 34px; height: 6px;
    background: var(--brand-blue);
  }
  .contact {
    position: absolute;
    left: 345px; top: 215px;
    list-style: none;
    margin: 0; padding: 0;
    font-size: 19px;
    color: var(--ink-gray);
  }
  .contact li {
    display: flex;
    align-items: center;
    gap: 10px;
    margin-bottom: 6px;
  }
  .contact svg { width: 14px; height: 14px; fill: var(--ink-dark); flex: none; }
</style>
</head>
<body>
<main class="canvas">

  <section class="card card--front" aria-label="Business card front">
    <div class="shard-band" role="img" aria-label="Translucent blue geometric shard pattern"></div>
    <div class="brand">
      <div class="brand__name"><span class="brand__mark"></span>Marrowgate Auctions</div>
      <div class="brand__tagline">Better Benefit Auctions Across the Land</div>
    </div>
  </section>

  <section class="card card--back" aria-label="Business card back">
    <div class="shard-band" role="img" aria-label="Translucent blue geometric shard pattern"></div>
    <div class="person">
      <div class="person__name">Owen <span>Tallis</span></div>
      <div class="person__title">Owner/President - Auctioneer</div>
    </div>
    <ul class="contact">
      <li>
        <svg viewBox="0 0 24 24" aria-hidden="true"><path d="M6.6 10.8a15.1 15.1 0 0 0 6.6 6.6l2.2-2.2c.3-.3.7-.4 1-.2 1.1.4 2.3.6 3.6.6.6 0 1 .4 1 1V20c0 .6-.4 1-1 1A17 17 0 0 1 3 4c0-.6.4-1 1-1h3.5c.6 0 1 .4 1 1 0 1.3.2 2.5.6 3.6.1.3 0 .7-.2 1z"/></svg>
        555-014-2290
      </li>
      <li>
        <svg viewBox="0 0 24 24" aria-hidden="true"><path d="M2 5h20v14H2z M4 7v.5l8 5 8-5V7l-8 5z" fill-rule="evenodd"/></svg>
        marrowgate@mailbox.com
      </li>
      <li>
        <svg viewBox="0 0 24 24" aria-hidden="true"><path d="M5 2l14 10-6 1 4 8-3 1.5-4-8-5 4z"/></svg>
        http://gavelrelief.com/
      </li>
    </ul>
  </section>

</main>
</body>
</html>
```